create clean, simple business card template

using the logo created now we need to create a simple, elegant business card design to suit

Industry/Entity Type

Business

Font styles to use
Other font styles liked:
• segoe ui

Requirements
Must have
• Front:
"Name:"
"Title:"
"Mobile:"
"email:"
and the logo

Back:
Logo
Nice to have
• Text in black but other graphics etc to match colours in logo as provided

```html
<!DOCTYPE html>
<html lang="en">
<head>
<meta charset="utf-8">
<title>K&amp;L Estates – Business Card</title>
<link rel="stylesheet" href="https://fonts.googleapis.com/css2?family=Open+Sans:ital,wght@0,400;0,600;0,700;1,400&display=swap">
<style>
  :root {
    --bg: #ece7de;
    --card: #ffffff;
    --shadow: #2b2520;
    --olive: #7b6b33;
    --olive-soft: #b3a674;
    --ink: #111111;
  }
  * { margin: 0; padding: 0; box-sizing: border-box; }
  html, body { width: 1200px; height: 782px; overflow: hidden; }
  body {
    background: var(--bg);
    font-family: "Open Sans", "Segoe UI", sans-serif;
    color: var(--ink);
    position: relative;
  }
  .card {
    position: absolute;
    top: 225px;
    width: 530px;
    height: 295px;
    background: var(--card);
    box-shadow: 6px 6px 0 var(--shadow);
    overflow: hidden;
  }
  .card--front { left: 40px; }
  .card--back { left: 595px; }

  .artwork {
    position: absolute;
    bottom: 0;
    left: 0;
    background: linear-gradient(180deg, var(--olive-soft) 0%, var(--olive) 100%);
  }
  .card--front .artwork { width: 250px; height: 168px; }
  .card--back .artwork { width: 485px; height: 155px; }

  .holder { position: absolute; left: 47px; top: 40px; }
  .holder__name { font-size: 19px; font-weight: 700; line-height: 1.1; }
  .holder__title { font-size: 15px; font-style: italic; line-height: 1.3; }

  .brand {
    display: flex; align-items: center; gap: 8px;
    color: var(--olive); font-weight: 600; white-space: nowrap;
  }
  .brand__dot { border-radius: 50%; background: var(--olive); }
  .card--front .brand { position: absolute; right: 42px; top: 30px; font-size: 24px; }
  .card--front .brand__dot { width: 14px; height: 14px; }
  .card--back .brand { position: absolute; left: 0; right: 0; top: 58px; justify-content: center; font-size: 44px; }
  .card--back .brand__dot { width: 24px; height: 24px; }

  .address {
    position: absolute; right: 42px; top: 84px;
    font-size: 8px; line-height: 1.3; text-align: right;
  }
  .contact {
    position: absolute; left: 275px; top: 167px;
    font-size: 13.5px; line-height: 18px;
  }
  .contact__row { display: flex; }
  .contact__label { width: 76px; }
</style>
</head>
<body>
  <section class="card card--front">
    <div class="artwork" role="img" aria-label="Illustration of a house roof with a window"></div>
    <div class="holder">
      <p class="holder__name">Daniel Marsh</p>
      <p class="holder__title">position</p>
    </div>
    <div class="brand"><span class="brand__dot"></span>K&amp;L ESTATES</div>
    <p class="address">2210 Lakeview Harbor road 14.<br>Norland</p>
    <div class="contact">
      <p class="contact__row"><span class="contact__label">Phone:</span>+(710) 2 3810 440 21</p>
      <p class="contact__row"><span class="contact__label">Fax:</span>+(710) 2 3810 440 22</p>
      <p class="contact__row"><span class="contact__label">Mobile:</span>+(710) 30 612 4478</p>
      <p>daniel.marsh@klestates.com</p>
    </div>
  </section>

  <section class="card card--back">
    <div class="artwork" role="img" aria-label="Illustration of two joined house roofs with windows"></div>
    <div class="brand"><span class="brand__dot"></span>K&amp;L ESTATES</div>
  </section>
</body>
</html>
```